Clothing Brand E-Commerce Website Design

We would like you to provide an ecommerce design template in layered PSD for our clothing/fashion brand website called "FernQuill".
We want the site to have a simple but sleek design similar to the following sites:
http://www.threadorbit.example/
http://tovalenwick.example/
http://www.sadiplume.example/
We want it to look stunning and blow the example sites out of the water. For color scheme, please use your imagination and try to impress us with your creativity.
We like teal and beige pink, with teal dominant.
Teal #7AFFFF / #46C6C6
Beige/pink #FF7B7C / #C74646
We want you to develop the design for 3 pages:
1) Home Page
Samples:
http://www.threadorbit.example/
http://tovalenwick.example/
http://www.sadiplume.example/
2) Products List Page (e.g., lists all "Dresses" when category is selected)
http://www.threadorbit.example/shop/casual-dresses
http://www.sadiplume.example/index.php?main_page=index&cPath=3
http://tovalenwick.example/modest-dresses.html
http://www.lunahive88.example/Product/Category.aspx?br=lh8&category=dress_maxi
3) Product Detail Page (e.g., individual product page with "Add to Cart")
http://www.threadorbit.example/shop/dresses/willow-dawn-dress
http://tovalenwick.example/modest-dresses/modest-dress-opal.html
http://www.sadiplume.example/index.php?main_page=product_info&cPath=3&products_id=297
Industry/Entity Type
Fashion

```html
<!DOCTYPE html>
<html lang="en">
<head>
<meta charset="utf-8">
<title>FernQuill – Dress # 1</title>
<link href="https://fonts.googleapis.com/css2?family=Raleway:wght@400;500;600&family=Open+Sans:wght@400;600;700&family=Oswald:wght@500&display=swap" rel="stylesheet">
<style>
  :root {
    --ink: #111111;
    --dark: #232323;
    --muted: #888888;
    --nav-grey: #cccccc;
    --panel-grey: #e9e7e8;
    --price-grey: #c4c4c4;
    --price-red: #a3141a;
    --star: #f6b800;
    --star-edge: #d48a00;
    --white: #ffffff;
  }
  * { box-sizing: border-box; margin: 0; padding: 0; }
  html, body { width: 1200px; height: 1044px; overflow: hidden; background: var(--white); }
  body { position: relative; font-family: "Open Sans", Arial, sans-serif; color: var(--ink); }
  .abs { position: absolute; }

  .promo-bar { left: 0; top: 0; width: 1200px; height: 32px; background: var(--dark); color: #dddddd; font-size: 9px; }
  .promo-bar span { position: absolute; top: 10px; white-space: nowrap; }

  .welcome { left: 155px; top: 79px; font-size: 10px; white-space: nowrap; }
  .welcome b { font-weight: 700; font-size: 11px; }
  .brand { left: 0; width: 1200px; top: 52px; text-align: center; font-family: "Raleway", sans-serif; font-weight: 500; font-size: 46px; }
  .account-links { right: 152px; top: 57px; font-family: "Raleway", sans-serif; font-size: 9.5px; color: var(--muted); white-space: nowrap; }
  .account-links i { font-style: normal; margin: 0 9px; }
  .search { left: 866px; top: 95px; width: 174px; height: 25px; border: 1px solid #aaaaaa; font-size: 9px; color: var(--muted); padding: 7px 14px; }
  .search svg { position: absolute; right: 10px; top: 6px; }

  .main-nav { left: 156px; top: 133px; width: 888px; height: 20px; background: var(--nav-grey); display: flex; font-family: "Raleway", sans-serif; font-size: 11.5px; }
  .main-nav span { display: flex; align-items: center; justify-content: center; border-right: 2px solid var(--white); height: 100%; white-space: nowrap; }
  .main-nav span:last-child { border-right: none; }

  .product-photo { left: 156px; top: 205px; width: 227px; height: 382px; border: 2px solid #cfcfcf; padding: 6px; }
  .photo-fill { width: 100%; height: 100%; background: linear-gradient(180deg, #ffffff 0%, #d9f5f5 30%, #36cccc 60%, #ffffff 100%); }
  .thumb { top: 596px; width: 71px; height: 72px; border: 2px solid #cfcfcf; padding: 3px; }
  .thumb div { width: 100%; height: 100%; background: linear-gradient(180deg, #f4f4f4 0%, #7fe0e0 55%, #e8e8e8 100%); }

  .product-title { left: 397px; top: 199px; font-family: "Raleway", sans-serif; font-size: 34px; font-weight: 400; }
  .title-rule { left: 397px; top: 244px; width: 434px; height: 2px; background: var(--ink); }
  .rating { display: flex; gap: 1px; }
  .price-bar { left: 397px; top: 252px; width: 434px; height: 29px; background: var(--price-grey); }
  .price-bar .label { position: absolute; left: 6px; top: -2px; font-family: "Raleway", sans-serif; font-size: 28px; color: var(--white); }
  .price-bar .amount { position: absolute; right: 10px; top: 2px; font-family: "Raleway", sans-serif; font-size: 20px; color: var(--price-red); font-weight: 500; }
  .price-bar .amount small { font-size: 13px; }
  .description { left: 397px; top: 290px; font-size: 11px; line-height: 14px; white-space: nowrap; }
  .description p + p { margin-top: 14px; }

  .options { left: 397px; top: 440px; font-size: 10.5px; font-weight: 700; }
  .opt-label { position: absolute; left: 0; white-space: nowrap; }
  .select { position: absolute; left: 73px; height: 16px; border: 1px solid #9a9a9a; background: #e2e2e2; font-size: 10px; font-weight: 400; color: var(--muted); padding: 1px 4px; white-space: nowrap; }
  .select::after { content: "▼"; position: absolute; right: 0; top: 0; width: 16px; height: 14px; border-left: 1px solid #9a9a9a; font-size: 8px; text-align: center; line-height: 14px; color: #666; }

  .add-to-cart { left: 400px; top: 619px; width: 218px; height: 46px; background: #2b2b2b; color: var(--white); font-weight: 700; font-size: 24px; display: flex; align-items: center; padding-left: 10px; gap: 8px; white-space: nowrap; }

  .reviews { left: 155px; top: 697px; width: 676px; height: 236px; background: var(--panel-grey); }
  .reviews h2 { position: absolute; left: 10px; top: 8px; font-size: 24px; font-weight: 600; color: #333333; }
  .reviews .rule { position: absolute; left: 0; top: 44px; width: 100%; height: 1px; background: #444444; }
  .write-review { position: absolute; left: 444px; top: 13px; width: 125px; height: 26px; background: #2b2b2b; color: var(--white); font-size: 13.5px; font-weight: 700; display: flex; align-items: center; gap: 5px; padding-left: 5px; white-space: nowrap; }
  .share { position: absolute; left: 573px; top: 13px; width: 100px; height: 26px; border: 1px solid #8ea0c8; background: #dde4f2; display: flex; align-items: center; font-size: 11px; }
  .share .btn { background: #4a64a3; color: var(--white); height: 100%; display: flex; align-items: center; gap: 6px; padding: 0 8px 0 5px; font-weight: 600; }
  .share .btn i { width: 12px; height: 12px; background: var(--white); display: block; }
  .share .count { padding-left: 10px; color: #3b5998; font-weight: 700; }
  .review { position: absolute; left: 19px; display: flex; gap: 8px; font-size: 9.5px; line-height: 12.5px; color: #333333; }
  .avatar { width: 51px; height: 52px; border: 2px solid #d6d6d6; background: var(--white); padding: 4px; flex-shrink: 0; }
  .avatar div { width: 100%; height: 100%; background: #e4b9cc; }
  .review p { padding-top: 5px; white-space: nowrap; }

  .best-sale { left: 847px; top: 205px; width: 188px; height: 594px; border: 2px solid #333333; }
  .best-sale h3 { position: absolute; left: 14px; top: 8px; width: 157px; height: 31px; background: #333333; color: var(--white); font-family: "Oswald", sans-serif; font-weight: 500; font-size: 21px; text-align: center; line-height: 31px; letter-spacing: 0.5px; }
  .sale-photo { position: absolute; left: 31px; width: 124px; height: 204px; }
  .sale-name { position: absolute; left: 17px; font-size: 14px; color: #222; }
  .sale-price { position: absolute; right: 14px; font-size: 10px; color: var(--price-red); }
  .sale-stars { position: absolute; left: 17px; }

  .footer { left: 0; top: 978px; width: 1200px; height: 66px; background: var(--dark); color: var(--white); font-size: 9px; }
  .footer .links { position: absolute; left: 143px; top: 21px; white-space: nowrap; }
  .footer .legal { position: absolute; right: 155px; top: 20px; text-align: right; line-height: 19px; white-space: nowrap; }
  .footer .legal b { font-size: 11px; font-weight: 600; }
  .back-to-top { left: 583px; top: 951px; }
</style>
</head>
<body>

<svg width="0" height="0" style="position:absolute">
  <defs>
    <symbol id="star" viewBox="0 0 20 20">
      <path d="M10 1.2l2.7 5.6 6.1.8-4.5 4.2 1.1 6.1L10 15l-5.4 2.9 1.1-6.1L1.2 7.6l6.1-.8z" fill="var(--star)" stroke="var(--star-edge)" stroke-width="1"/>
    </symbol>
  </defs>
</svg>

<header>
  <div class="abs promo-bar">
    <span style="left:584px">Take and Extra 20% OFF Your Purchase - Code: June 14</span>
    <span style="left:856px">Call Customer Services on: +1-555-010-2290</span>
  </div>
  <div class="abs welcome">Welcome visitor you can <b>log in</b> or create an <b>account</b></div>
  <div class="abs brand">FernQuill</div>
  <div class="abs account-links">Order list<i>|</i>My Account<i>|</i>Checkout ( 0 )</div>
  <div class="abs search">Search . . .
    <svg width="11" height="11" viewBox="0 0 11 11"><circle cx="4.5" cy="4.5" r="3.5" fill="none" stroke="#111" stroke-width="1.6"/><line x1="7" y1="7" x2="10" y2="10" stroke="#111" stroke-width="1.8"/></svg>
  </div>
  <nav class="abs main-nav">
    <span style="width:93px">HOME</span>
    <span style="width:118px">WOMEN</span>
    <span style="width:103px">MEN</span>
    <span style="width:109px">PAGES</span>
    <span style="width:124px">CONTACT US</span>
    <span style="width:111px">FEATURES</span>
    <span style="width:129px">TYPOGRAPHY</span>
    <span style="width:101px">SHOP</span>
  </nav>
</header>

<main>
  <div class="abs product-photo"><div class="photo-fill" role="img" aria-label="Model wearing the teal and navy colour-block dress"></div></div>
  <div class="abs thumb" style="left:156px"><div role="img" aria-label="Dress front view thumbnail"></div></div>
  <div class="abs thumb" style="left:235px"><div role="img" aria-label="Dress side view thumbnail"></div></div>
  <div class="abs thumb" style="left:314px"><div role="img" aria-label="Dress flat view thumbnail"></div></div>

  <h1 class="abs product-title">Dress # 1</h1>
  <div class="abs rating" style="left:737px;top:224px">
    <svg width="19" height="19"><use href="#star"/></svg><svg width="19" height="19"><use href="#star"/></svg><svg width="19" height="19"><use href="#star"/></svg><svg width="19" height="19"><use href="#star"/></svg><svg width="19" height="19"><use href="#star"/></svg>
  </div>
  <div class="abs title-rule"></div>
  <div class="abs price-bar"><span class="label">Price</span><span class="amount"><small>$</small> 100 .00</span></div>
  <div class="abs description">
    <p>his is an amazing color-block dress! Made from a light Ponte that is easy to wear<br>and very, very comfortable. This cut is very flattering on every body type. The<br>banded waist accentuates, while the full skirt camouflages. The colors and style<br>of the Larkvale gives this dress a retro look which is a big trend. No zipper or<br>buttons. Pull-over dress.</p>
    <p>83%Poly 14%Rayon 3%Spandex, Wash cold, Hang to Dry. American fabric assem-<br>bled in Mexico.</p>
  </div>

  <div class="abs options">
    <span class="opt-label" style="top:0">Please Choose:</span>
    <span class="opt-label" style="top:27px">Colour :</span>
    <span class="select" style="top:26px;width:108px">Choose colour</span>
    <span class="opt-label" style="top:54px">Size :</span>
    <span class="select" style="top:52px;width:108px">Choose Size</span>
    <span class="opt-label" style="top:82px">Availability :&nbsp;&nbsp; In stock</span>
    <span class="opt-label" style="top:109px">Quantity :</span>
    <span class="select" style="top:107px;width:37px">0</span>
  </div>

  <div class="abs add-to-cart">ADD TO CART
    <svg width="38" height="34" viewBox="0 0 38 34"><path d="M2 8h6l4 16h18l4-12H10" fill="none" stroke="#fff" stroke-width="2.5"/><circle cx="14" cy="29" r="2.5" fill="#fff"/><circle cx="28" cy="29" r="2.5" fill="#fff"/><circle cx="30" cy="7" r="6" fill="#fff"/><path d="M30 3.5v7M26.5 7h7" stroke="#2b2b2b" stroke-width="2"/></svg>
  </div>

  <section class="abs reviews">
    <h2>Reviews</h2>
    <div class="write-review">
      <svg width="20" height="18" viewBox="0 0 20 18"><rect x="1" y="1" width="15" height="16" fill="none" stroke="#fff" stroke-width="1.5"/><path d="M4 6h9M4 9h9M4 12h6" stroke="#fff" stroke-width="1.2"/><path d="M12 14l7-10" stroke="#fff" stroke-width="2"/></svg>
      Write Review
    </div>
    <div class="share"><span class="btn"><i></i>Share</span><span class="count">2K</span></div>
    <div class="rule"></div>
    <div class="review" style="top:63px">
      <div class="avatar"><div role="img" aria-label="Reviewer avatar"></div></div>
      <p>Lorem ipsum dolor sit amet, consectetur adipisicing elit, sed do eiusmod tempor incididunt ut labore et dolore<br>magna aliqua. Lorem ipsum dolor sit amet, consectetur adipisicing elit, sed do eiusmod tempor incididunt ut labore<br>et dolore magna aliqua.</p>
    </div>
    <div class="review" style="top:149px">
      <div class="avatar"><div role="img" aria-label="Reviewer avatar"></div></div>
      <p>Lorem ipsum dolor sit amet, consectetur adipisicing elit, sed do eiusmod tempor incididunt ut labore et dolore magna<br>aliqua. Lorem ipsum dolor sit amet, consectetur adipisicing elit, sed do eiusmod tempor incididunt ut labore et dolore<br>magna aliqua. Lorem ipsum dolor sit amet, consectetur adipisicing elit, sed do eiusmod tempor incididunt ut labore et<br>dolore magna aliqua.</p>
    </div>
  </section>

  <aside class="abs best-sale">
    <h3>BEST SALE</h3>
    <div class="sale-photo" style="top:57px;background:linear-gradient(180deg,#ffffff 0%,#e9e2c0 40%,#f2b820 80%,#ffffff 100%)" role="img" aria-label="Model in yellow cardigan and yellow skirt"></div>
    <span class="sale-name" style="top:268px">Dress # 1</span>
    <span class="sale-price" style="top:270px">$ 100</span>
    <div class="sale-stars rating" style="top:286px">
      <svg width="18" height="18"><use href="#star"/></svg><svg width="18" height="18"><use href="#star"/></svg><svg width="18" height="18"><use href="#star"/></svg><svg width="18" height="18"><use href="#star"/></svg><svg width="18" height="18"><use href="#star"/></svg>
    </div>
    <div class="sale-photo" style="top:331px;background:linear-gradient(180deg,#c9b7a8 0%,#d83fa0 35%,#8d8d8d 70%,#7a6d60 100%)" role="img" aria-label="Model in pink jacket and striped pencil skirt"></div>
    <span class="sale-name" style="top:543px">Dress # 1</span>
    <span class="sale-price" style="top:545px">$ 100</span>
    <div class="sale-stars rating" style="top:561px">
      <svg width="18" height="18"><use href="#star"/></svg><svg width="18" height="18"><use href="#star"/></svg><svg width="18" height="18"><use href="#star"/></svg><svg width="18" height="18"><use href="#star"/></svg><svg width="18" height="18"><use href="#star"/></svg>
    </div>
  </aside>
</main>

<svg class="abs back-to-top" width="34" height="27" viewBox="0 0 34 27"><path d="M17 0L34 27H0z" fill="var(--dark)"/><path d="M17 12v11M11.5 17.5h11" stroke="#fff" stroke-width="2.4"/></svg>
<footer class="abs footer">
  <div class="links">Privacy &amp; Cookies Terms &amp; Conditions Accessibility Store Directory About Us</div>
  <div class="legal"><b>©2014 FernQuill Shop Ltd</b><br>All rights reserved</div>
</footer>

</body>
</html>
```